Fundraising Study Day East of England. Lift the January blues!

A flyer to advertise a fundraising event of lectures for dental hygienists and therapists in support of the exemption campaign. Currently dental hygienists and therapists require a prescription to deliver certain treatment or recommend certain toothpastes. If we are successful in the campaign we will be able to treat patients without these restrictions.

Dental

```html
<!DOCTYPE html>
<html lang="en">
<head>
<meta charset="utf-8">
<title>Fundraising Study Day East of England</title>
<link rel="stylesheet" href="https://fonts.googleapis.com/css2?family=Cabin:wght@600&family=Lato:wght@400;700;900&display=swap">
<style>
:root{
  --navy:#0f2d5c;
  --blue:#1468b4;
  --bright:#1a73c6;
  --yellow:#d6e024;
  --ink:#2e3440;
  --pale:#e6f1fa;
  --paler:#f4f9fd;
  --white:#ffffff;
}
*{margin:0;padding:0;box-sizing:border-box}
html,body{width:946px;height:1200px;overflow:hidden;background:var(--white)}
.flyer{position:relative;width:946px;height:1200px;overflow:hidden;
  background:linear-gradient(160deg,var(--paler) 0%,var(--pale) 55%,#d3e6f5 100%);
  font-family:'Lato',sans-serif;color:var(--ink)}
.header{position:absolute;left:0;top:0;width:946px;height:406px}
.header svg{position:absolute;left:0;top:0}
.title{position:absolute;left:46px;top:52px;width:440px;font-family:'Cabin',sans-serif;font-weight:600;
  font-size:39px;line-height:44px;color:var(--yellow)}
.description{position:absolute;left:48px;top:214px;width:410px;color:var(--white);font-size:15.5px;line-height:20.2px}
.description .label{color:var(--yellow);font-size:16px;text-transform:uppercase;margin-bottom:1px}
.facts{position:absolute;top:411px;left:0;width:946px}
.fact{position:absolute;top:0;height:147px;border-radius:0 0 7px 7px;
  background:linear-gradient(180deg,var(--blue) 0%,var(--navy) 100%);color:var(--white);text-align:center;
  box-shadow:0 3px 6px rgba(15,45,92,.25)}
.fact svg{display:block;margin:16px auto 0}
.fact h3{font-weight:400;color:var(--yellow);font-size:22px;line-height:24px;margin-top:6px}
.fact p{font-size:15.5px;line-height:20.5px}
.fact .price{font-size:25px;font-weight:900;margin-top:3px}
.fact-location{left:84px;width:267px}
.fact-date{left:375px;width:267px}
.fact-cost{left:668px;width:190px}
.agenda-title{position:absolute;left:74px;top:592px;font-size:25px;font-weight:700;color:var(--navy)}
.dental-scene{position:absolute;left:0;top:920px;width:470px;height:204px;
  background:radial-gradient(ellipse at 45% 60%,#f4f8fb 0%,#cfdceb 45%,rgba(211,230,245,0) 75%)}
.slot{position:absolute;width:380px;font-size:15.5px;line-height:20.3px}
.slot .time{color:var(--bright);font-size:20px;font-weight:700;line-height:24px;margin-right:8px}
.slot .time.block{display:block}
.col-left{left:74px}
.col-right{left:502px;width:378px}
.footer{position:absolute;left:0;top:1124px;width:946px;height:76px;
  background:linear-gradient(90deg,var(--navy) 0%,var(--blue) 100%);display:flex;align-items:center;justify-content:center}
.footer a{color:var(--yellow);font-size:14px;text-decoration:none;letter-spacing:.1px}
</style>
</head>
<body>
<div class="flyer">
  <header class="header">
    <svg width="946" height="406" viewBox="0 0 946 406">
      <defs>
        <linearGradient id="photoTone" x1="0" y1="0" x2="1" y2="1">
          <stop offset="0" stop-color="#e9eef2"/>
          <stop offset=".55" stop-color="#cfd9e2"/>
          <stop offset="1" stop-color="#b7c6d2"/>
        </linearGradient>
        <linearGradient id="panelTone" x1="0" y1="0" x2="1" y2="0.3">
          <stop offset="0" stop-color="#0f2d5c"/>
          <stop offset=".6" stop-color="#154f8f"/>
          <stop offset="1" stop-color="#1a6fbf"/>
        </linearGradient>
      </defs>
      <rect x="300" y="0" width="646" height="406" fill="url(#photoTone)" role="img" aria-label="Photo of a smiling dental professional with arms folded, a hygienist treating a patient in the surgery chair behind him"/>
      <polygon points="0,0 603,0 403,406 0,406" fill="url(#panelTone)"/>
      <polygon points="0,406 150,406 0,300" fill="#0c2550" opacity=".35"/>
    </svg>
    <h1 class="title">Fundraising Study Day East of England. Lift the January blues!</h1>
    <div class="description">
      <p class="label">Description</p>
      <p>A fundraising event to support our exemptions project. The day will consist of a series of presentations ranging from the new ECPD to new technologies. The aim, being to enhance our learning and raise funds to support the exemptions campaign. The speaker line includes some of the UK and Irelands most respected dental prefossionals in our field.</p>
    </div>
  </header>

  <section class="facts">
    <div class="fact fact-location">
      <svg width="52" height="50" viewBox="0 0 52 50" fill="none" stroke="#fff" stroke-width="3.5" aria-hidden="true">
        <path d="M26 34 C18 24 15 19 15 14 a11 11 0 0 1 22 0 c0 5-3 10-11 20z"/>
        <circle cx="26" cy="14" r="4"/>
        <path d="M16 30 C6 33 4 37 6 40 c4 6 36 6 40 0 c2-3 0-7-10-10"/>
      </svg>
      <h3>LOCATION</h3>
      <p>Elmfield Hotel, Meteor Road,<br>Hatfield, AL10 4QX</p>
    </div>
    <div class="fact fact-date">
      <svg width="52" height="50" viewBox="0 0 52 50" fill="none" stroke="#fff" stroke-width="3" aria-hidden="true">
        <rect x="6" y="8" width="34" height="32" rx="4"/>
        <line x1="6" y1="16" x2="40" y2="16"/>
        <line x1="14" y1="4" x2="14" y2="11"/><line x1="23" y1="4" x2="23" y2="11"/><line x1="32" y1="4" x2="32" y2="11"/>
        <g fill="#fff" stroke="none"><rect x="11" y="21" width="4" height="4"/><rect x="19" y="21" width="4" height="4"/><rect x="27" y="21" width="4" height="4"/><rect x="11" y="29" width="4" height="4"/><rect x="19" y="29" width="4" height="4"/></g>
        <circle cx="38" cy="37" r="9" fill="#164c8a"/>
        <path d="M38 32 v5 h4"/>
      </svg>
      <h3>DATE AND TIME</h3>
      <p>Fri 19 January 2018<br>09:00 – 16:30 GMT</p>
    </div>
    <div class="fact fact-cost">
      <svg width="56" height="50" viewBox="0 0 56 50" fill="none" stroke="#fff" stroke-width="3" aria-hidden="true">
        <circle cx="22" cy="22" r="15"/>
        <text x="22" y="29" text-anchor="middle" fill="#fff" stroke="none" font-family="Lato,sans-serif" font-weight="900" font-size="20">$</text>
        <rect x="30" y="34" width="6" height="11" fill="#fff" stroke="none"/>
        <path d="M38 45 h9 c2 0 3-2 3-4 l0-5 c0-2-2-3-4-3 h-4 l1-5 c0-2-3-3-4-1 l-3 6 v12z" fill="#fff" stroke="none"/>
      </svg>
      <h3>COST</h3>
      <p class="price">£101.48</p>
    </div>
  </section>

  <h2 class="agenda-title">AGENDA</h2>
  <div class="dental-scene" role="img" aria-label="Soft image of a dental handpiece, a tooth, a mouth mirror and pearls"></div>

  <div class="slot col-left" style="top:645px">
    <span class="time block">9.30 - 10.15</span>
    Helen Marsh: Immediate past president of the BDTG will be updating us on all things ECPD
  </div>
  <div class="slot col-left" style="top:731px">
    <span class="time block">10.15 - 11.00</span>
    Laura Penfold: Will provide an update on teeth whiteing and explain how social media has impacted her business<br>
    Clare Whitby: Our internationally acclaimed speaker will update our knowledge of periodontal disease and nutrition and new technologies.
  </div>
  <div class="slot col-left" style="top:897px"><span class="time">9.30 - 10.15</span>Break</div>

  <div class="slot col-right" style="top:645px">
    <span class="time block">11.30 - 13.00</span>
    Nadia Brennan &amp; Rosa Kingsley: Will be providing a combined presentation on 'Scaling your business' and start to finish Sonivex techniques. The aim being to build our business with effective communications, systems and protocols. This sessions promises audience participation!
  </div>
  <div class="slot col-right" style="top:815px"><span class="time">12 - 1400</span>lunch</div>
  <div class="slot col-right" style="top:861px">
    <span class="time block">14 - 15.00</span>
    Jo Marlow: Save your back. All things posture.
  </div>
  <div class="slot col-right" style="top:926px"><span class="time">15.00 - 15.30</span>Break</div>
  <div class="slot col-right" style="top:972px">
    <span class="time block">15.30 -16.30</span>
    Clare Whitby: Our internationally acclaimed speaker will update our knowledge of periodontal disease and nutrition and new technologies.
  </div>

  <footer class="footer">
    <a href="https://www.eventpass.co.uk/e/fundraising-study-day-east-of-england-lift-the-january-blues-tickets-48213057916">https://www.eventpass.co.uk/e/fundraising-study-day-east-of-england-lift-the-january-blues-tickets-48213057916</a>
  </footer>
</div>
</body>
</html>
```